Upgrades and adjustments to my existing website

I currently have a website in the trial period with HostBramble but their template isn't meeting my site needs. My website is https://www.QuorvaPosts.example. I need the calendar to be changed. Each customer that orders a real estate sign installation from us needs to be able to request a day (not time specific) and be able to enter the address of the home where they need the sign installed. In addition, I would like a testimonials section on the website. I need someone to build the website and point it to my domain name as I do not know how to do any of that. My customers are trying to order now so every day they can't place the order I am losing money so quick turn time is important

Target Market(s)

Real Estate Agents ordering sign post installations

Industry/Entity Type

Real Estate

Coding

Coded - Design and coding required

Number of Pages Required

1 page

Font styles to use
Sans Serif

Colors
0355a3
3377b5
85abd2
0493ce
33a6d7
85cae6

Requirements
Must have
• The ability to book installation requests online with address for installation. Please see live current website I have
Nice to have
• Links to social media, ability to pay invoice on website,
Testimonial section.
Ability to track progress of installation request for customers
Ability to share the appointment calendar with my installers

```html
<!DOCTYPE html>
<html lang="en">
<head>
<meta charset="utf-8">
<title>Quorva Posts – Book Now</title>
<link href="https://fonts.googleapis.com/css2?family=Mulish:wght@400;600;700&family=Montserrat:wght@400;500;600&display=swap" rel="stylesheet">
<style>
:root{
  --navy:#132f47;
  --navy-footer:#14304a;
  --navy-deep:#0b2638;
  --page:#f2f9fe;
  --ink:#1d2b38;
  --muted:#8a96a0;
  --field-line:#b9c3cc;
  --accent:#2f8fe8;
  --sky:#33a6d7;
  --cyan:#0493ce;
  --white:#ffffff;
}
*{box-sizing:border-box;margin:0;padding:0}
html,body{width:1200px;height:978px;overflow:hidden}
body{position:relative;background:var(--page);font-family:"Mulish",sans-serif;color:var(--ink)}
.abs{position:absolute}

/* header */
.site-header{position:absolute;left:0;top:0;width:1200px;height:138px;background:var(--navy)}
.brand{position:absolute;left:212px;top:52px;display:flex;align-items:center;gap:7px;color:var(--white);font-family:"Montserrat",sans-serif;font-weight:600;font-size:17px}
.brand-mark{width:14px;height:14px;background:var(--accent)}
.main-nav{position:absolute;top:74px;left:0;font-family:"Montserrat",sans-serif;font-size:11px;color:var(--white)}
.main-nav a{position:absolute;white-space:nowrap;color:inherit;text-decoration:none}
.main-nav a.is-active{color:var(--sky)}

/* booking summary */
.service-title{left:231px;top:179px;font-size:13px;font-weight:700;letter-spacing:.3px}
.service-meta{left:231px;top:198px;font-size:13px;letter-spacing:.3px}
.detail{font-size:13.5px;letter-spacing:.3px;left:231px}
.detail b{color:var(--accent);font-weight:700}
.photo-frame{left:231px;top:303px;width:194px;height:175px;background:var(--white);box-shadow:0 0 3px rgba(0,0,0,.25)}
.photo{position:absolute;left:7px;top:7px;width:180px;height:161px;background:linear-gradient(90deg,#7c8a94 0%,#e9eef2 30%,#f7f9fa 55%,#9aa4ab 80%,#6f7a82 100%)}

/* form */
.form-title{left:596px;top:173px;font-size:13.5px;font-weight:700;letter-spacing:.3px}
.field{position:absolute;left:595px;width:387px;height:38px;border:1.5px solid var(--field-line);background:transparent;padding-left:12px;font-family:"Mulish",sans-serif;font-size:9.5px;color:var(--muted);display:flex;align-items:center}
.confirm-btn{left:595px;top:587px;width:209px;height:40px;background:var(--navy);color:var(--white);font-family:"Montserrat",sans-serif;font-size:15px;font-weight:500;letter-spacing:.6px;display:flex;align-items:center;justify-content:center;box-shadow:0 0 0 1px var(--white)}

/* footer */
.site-footer{position:absolute;left:0;top:673px;width:1200px;height:243px;background:var(--navy-footer);color:var(--white);font-family:"Montserrat",sans-serif}
.footer-brand{left:218px;top:36px;font-size:16px;font-weight:500}
.footer-text{font-size:9.5px;line-height:15px}
.footer-head{font-size:9.5px;font-weight:500;top:54px;letter-spacing:.2px}
.social{position:absolute;top:175px;width:23px;height:23px;border-radius:50%;background:var(--sky)}
.subscribe-box{left:810px;top:118px;width:187px;height:37px;border:1.5px solid #6b7f91}
.subscribe-box span{position:absolute;left:7px;top:12px;font-size:9px}
.send-btn{position:absolute;right:3px;top:6px;width:40px;height:24px;background:var(--cyan);display:flex;align-items:center;justify-content:center}
.copyright-bar{position:absolute;left:0;top:916px;width:1200px;height:62px;background:var(--navy-deep);color:var(--white);font-family:"Montserrat",sans-serif;font-size:11px;display:flex;align-items:center;justify-content:center}
</style>
</head>
<body>

<header class="site-header">
  <div class="brand"><span class="brand-mark"></span>Quorva Posts</div>
  <nav class="main-nav">
    <a style="left:539px">HOME</a>
    <a style="left:595px">ABOUT US</a>
    <a style="left:672px">SERVICES</a>
    <a style="left:747px">TESTIMONIALS</a>
    <a style="left:845px" class="is-active">BOOK NOW</a>
    <a style="left:930px">CONTACT US</a>
  </nav>
</header>

<main>
  <section class="booking-summary">
    <div class="abs service-title">Real Estate Sign Installation</div>
    <div class="abs service-meta">1 hr|Price varies</div>
    <div class="abs detail" style="top:228px"><b>Booking Date:</b> 24-03-2021</div>
    <div class="abs detail" style="top:256px"><b>Associated Staff:</b> Dana Morrow</div>
    <div class="abs photo-frame">
      <div class="photo" role="img" aria-label="White wooden sign posts stacked in a storage shed"></div>
    </div>
  </section>

  <section class="client-form">
    <div class="abs form-title">Client Information</div>
    <div class="field" style="top:206px">Your name</div>
    <div class="field" style="top:258px">Your email</div>
    <div class="field" style="top:311px">Phone No</div>
    <div class="field" style="top:363px">Address Line 1</div>
    <div class="field" style="top:416px">Address Line 2</div>
    <div class="field" style="top:468px">Zip Code</div>
    <div class="field" style="top:521px">Specal Note</div>
    <div class="abs confirm-btn">CONFIRM BOOKING</div>
  </section>
</main>

<footer class="site-footer">
  <div class="abs footer-brand">Quorva Posts</div>
  <p class="abs footer-text" style="left:218px;top:81px;width:215px">We install solar powered lit real estate signs to make your home stand out and get it sold. We use treated wood posts with powder-coated steel bases for high quality, looks and durability.</p>
  <span class="social" style="left:220px"></span>
  <span class="social" style="left:245px"></span>
  <span class="social" style="left:270px"></span>
  <span class="social" style="left:295px"></span>
  <span class="social" style="left:320px"></span>

  <div class="abs footer-head" style="left:467px">CONTACT INFO</div>
  <p class="abs footer-text" style="left:468px;top:81px">555-014-2290<br>orders@quorvaposts.example<br>www.quorvaposts.example</p>

  <div class="abs footer-head" style="left:617px">OFFICE HOURS</div>
  <p class="abs footer-text" style="left:617px;top:81px;line-height:19px">Mon- Fri - 9:00 am - 5:00pm<br>Saturday- 9:00 am - 2:00 pm<br>Sunday- Closed</p>

  <div class="abs footer-head" style="left:809px">SUBSCRIBE NEWSLETTERS</div>
  <p class="abs footer-text" style="left:810px;top:81px;width:185px">Stay always in touch, subscribe to our newsletters</p>
  <div class="abs subscribe-box">
    <span>your email id</span>
    <div class="send-btn">
      <svg width="10" height="10" viewBox="0 0 10 10"><path d="M9.5 0.5 L0.5 4.2 L4.3 5.7 L5.8 9.5 Z" fill="#fff"/></svg>
    </div>
  </div>
  <p class="abs footer-text" style="left:810px;top:170px">Don't worry, we don't span</p>
</footer>

<div class="copyright-bar">© 2021, Quorva Posts, all Rights reserved</div>

</body>
</html>
```